Binder design for a veterinary clinic

We are seeking a talented designer to create a standout design for ring binders specifically for our veterinary clinic. These binders will be used to organize materials from our Continuing Professional Development (CPD) projects for colleagues and interns. The design should be clean, professional, and align with our brand guidelines. To give you a better understanding of our branding, we’ve included the design of our vehicles as a reference. As additional reference, please visit www.tierpraxoland.at

Target Market(s)

veterinarians

Industry/Entity Type

Veterinary

Font styles to use
Sans Serif

Colors
0054AA
0677BA
7BADD7
CADEEF
E8F1F8
FFC000
F8CF3A
FAE287
FDF2CF
FEFAEE

Requirements
Must have
• Our Logo an a clean design
Should not have
• to much images

```html
<!DOCTYPE html>
<html lang="de">
<head>
<meta charset="utf-8">
<title>Tierpraxoland – Ordner</title>
<link href="https://fonts.googleapis.com/css2?family=Poppins:wght@500;600&display=swap" rel="stylesheet">
<style>
  :root {
    --backdrop: #ececec;
    --navy: #2a3d51;
    --navy-deep: #1f2c3b;
    --gold: #dba123;
    --paper: #f3f3f1;
    --paper-shade: #e2e2df;
    --ring: #b9bcc0;
    --white: #ffffff;
  }
  html, body {
    margin: 0;
    width: 1200px;
    height: 900px;
    overflow: hidden;
    background: var(--backdrop);
    font-family: "Poppins", Arial, sans-serif;
  }
  .binder {
    position: absolute;
    left: 170px;
    top: 70px;
    width: 860px;
    height: 760px;
    display: flex;
    box-shadow: 0 20px 40px rgba(0,0,0,.18);
  }
  .spine {
    position: relative;
    width: 200px;
    height: 100%;
  }
  .cover {
    position: relative;
    width: 660px;
    height: 100%;
  }
  .spine svg, .cover svg { position: absolute; inset: 0; }
  .brand-name {
    margin: 0;
    font-weight: 600;
    color: var(--white);
    line-height: 1;
    letter-spacing: -0.5px;
    white-space: nowrap;
  }
  .brand-tagline {
    margin: 5px 0 0;
    font-weight: 500;
    color: var(--gold);
    line-height: 1.1;
    white-space: nowrap;
  }
  .cover-brand {
    position: absolute;
    right: 60px;
    top: 48px;
    text-align: left;
  }
  .cover-brand .brand-name { font-size: 30px; }
  .cover-brand .brand-tagline { font-size: 13px; }
  .spine-brand {
    position: absolute;
    left: 0;
    right: 0;
    top: 470px;
    text-align: center;
  }
  .spine-brand .brand-name { font-size: 22px; color: var(--navy-deep); }
  .spine-brand .brand-tagline { font-size: 10px; }
</style>
</head>
<body>
  <div class="binder">
    <section class="spine">
      <svg width="200" height="760" viewBox="0 0 200 760">
        <rect width="200" height="760" fill="var(--navy-deep)"/>
        <path d="M0 70 Q100 44 200 40 L200 708 Q100 706 0 690 Z" fill="var(--gold)"/>
        <path d="M0 84 Q100 60 200 56 L200 690 Q100 690 0 674 Z" fill="var(--paper)"/>
        <path d="M30 150 Q30 120 60 120 L200 120 L200 400 L60 400 Q30 400 30 370 Z" fill="var(--paper-shade)" role="img" aria-label="Platz für Illustration: Hund im Profil"/>
        <circle cx="100" cy="640" r="28" fill="var(--navy-deep)"/>
        <circle cx="100" cy="640" r="28" fill="none" stroke="var(--ring)" stroke-width="5"/>
      </svg>
      <div class="spine-brand">
        <p class="brand-name">Tierpraxoland</p>
        <p class="brand-tagline">Fachklinik für Kleintiere</p>
      </div>
    </section>
    <section class="cover">
      <svg width="660" height="760" viewBox="0 0 660 760">
        <defs>
          <clipPath id="arc-inner">
            <path d="M0 80 C230 80 512 318 512 560 C512 672 450 740 400 760 L0 760 Z"/>
          </clipPath>
        </defs>
        <rect width="660" height="760" fill="var(--navy)"/>
        <path d="M0 40 C260 40 560 300 560 560 C560 690 480 760 420 760 L0 760 Z" fill="var(--gold)"/>
        <path d="M0 54 C250 54 544 306 544 560 C544 680 470 748 416 760 L0 760 Z" fill="var(--white)"/>
        <path d="M0 80 C230 80 512 318 512 560 C512 672 450 740 400 760 L0 760 Z" fill="var(--navy)"/>
        <g clip-path="url(#arc-inner)">
          <path d="M0 120 L200 120 Q240 120 240 160 L240 360 Q240 400 200 400 L0 400 Z" fill="var(--paper-shade)" role="img" aria-label="Platz für Illustration: Hund im Profil"/>
          <rect x="300" y="270" width="170" height="520" rx="70" fill="var(--gold)" role="img" aria-label="Platz für Illustration: Katze als Silhouette"/>
        </g>
      </svg>
      <div class="cover-brand">
        <p class="brand-name">Tierpraxoland</p>
        <p class="brand-tagline">Fachklinik für Kleintiere</p>
      </div>
    </section>
  </div>
</body>
</html>
```